Gobal construction supply company needs new business card design

I need a business card design for my global supply company using an existing logo. i will be looking to print these on rounded corner cards with the black background version of my logo on the back. on the front white background, my logo again and my simple details.

```html
<!DOCTYPE html>
<html lang="en">
<head>
<meta charset="utf-8">
<title>Meridian Build Supply – Business Cards</title>
<link rel="stylesheet" href="https://fonts.googleapis.com/css2?family=Figtree:wght@400;600;700&display=swap">
<style>
  :root {
    --page: #e9e6e2;
    --card-dark: #1c1c1f;
    --card-light: #f1f1f1;
    --ink: #2a2a2d;
    --ink-soft: #3b3b3f;
    --red: #d41f26;
    --white: #ffffff;
  }
  * { box-sizing: border-box; margin: 0; padding: 0; }
  html, body {
    width: 1200px; height: 960px; overflow: hidden;
    background: var(--page);
    font-family: "Figtree", "Helvetica Neue", Arial, sans-serif;
  }
  .canvas { position: relative; width: 1200px; height: 960px; }

  .card {
    position: absolute;
    width: 570px; height: 334px;
    border-radius: 12px;
    overflow: hidden;
    box-shadow: 0 6px 18px rgba(0,0,0,.18);
  }

  /* Back side */
  .card-back {
    left: 150px; top: 80px;
    background: var(--card-dark);
    display: flex; align-items: center; justify-content: center;
  }
  .brand {
    display: flex; align-items: center; gap: 10px;
    font-weight: 700; text-transform: uppercase; letter-spacing: .02em;
  }
  .brand-mark { width: 14px; height: 14px; background: var(--red); flex: none; }
  .card-back .brand { color: var(--white); font-size: 21px; }

  /* Front side */
  .card-front {
    left: 480px; top: 500px;
    background: var(--card-light);
  }
  .front-logo {
    position: absolute; left: 24px; top: 80px; width: 240px;
  }
  .card-front .brand { color: var(--ink); font-size: 17px; }
  .divider {
    position: absolute; left: 284px; top: 60px;
    width: 1.5px; height: 216px; background: var(--ink-soft);
  }
  .details {
    position: absolute; left: 303px; top: 60px;
    color: var(--ink); font-size: 14.5px; line-height: 1.45;
  }
  .name { color: var(--red); font-weight: 600; font-size: 17px; line-height: 1.3; }
  .role { font-size: 17px; line-height: 1.3; margin-bottom: 14px; }
  .address { margin-bottom: 14px; }
  .contact-row { display: flex; }
  .contact-row .label { font-weight: 700; width: 20px; }
  .contact-row .sep { width: 12px; }
  .phones { margin-bottom: 14px; }
  .base-band { position: absolute; left: 0; bottom: 0; width: 100%; height: 12px; }
</style>
</head>
<body>
<main class="canvas">

  <section class="card card-back" aria-label="Card back">
    <div class="brand"><span class="brand-mark"></span>Meridian Build Supply</div>
  </section>

  <section class="card card-front" aria-label="Card front">
    <div class="front-logo">
      <div class="brand"><span class="brand-mark"></span>Meridian Build Supply</div>
    </div>

    <div class="divider"></div>

    <div class="details">
      <p class="name">Your Full Name</p>
      <p class="role">Director</p>
      <p class="address">Your Company Address,<br>Eastwood NSW 2122, Australia.</p>
      <div class="phones">
        <p class="contact-row"><span class="label">M</span><span class="sep">:</span>+61 400 555 018</p>
        <p class="contact-row"><span class="label">T</span><span class="sep">:</span>+61 2 5550 1234</p>
      </div>
      <p class="contact-row"><span class="label">E</span><span class="sep">:</span>info@meridianbuild.example</p>
      <p class="contact-row"><span class="label">W</span><span class="sep">:</span>www.meridianbuild.example</p>
    </div>

    <svg class="base-band" viewBox="0 0 570 12" preserveAspectRatio="none" aria-hidden="true">
      <polygon points="0,0 288,0 284,12 0,12" fill="var(--red)"/>
      <polygon points="291,0 570,0 570,12 287,12" fill="var(--card-dark)"/>
    </svg>
  </section>

</main>
</body>
</html>
```